Quorvel Properties - Chat n’ Clink Evening Graphic Invite

We need a graphic design for a corporate reception that we are calling Chat n’ Clink Evening. The invite should read:

"QVR invites you to join us at Chat n’ Clink Evening

Monday, Jan 22nd
6:30 - 8:30 pm EST

Tallow Grill - Lounge Room

48213 E Harrow Glen Rd
Aventura, FL 33417

Join us for excellent wine and tasty bites at our semi-annual PDA reception. Swing by whenever you can – timing is casual and we'd love to see you there!"

Please feel free to use fun photos from the Tallow Grill gallery: https://www.tallowgrillexample.com/photos

Also, please use the QVR logo attached.

Target Market(s)

Corporate professional

Colors
0054AA
0677BA
7BADD7
CADEEF
E8F1F8

Requirements
Must have
• QVR logo, attached verbiage

```html
<!DOCTYPE html>
<html lang="en">
<head>
<meta charset="utf-8">
<title>QVR – Chat n’ Clink Evening</title>
<link rel="stylesheet" href="https://fonts.googleapis.com/css2?family=Great+Vibes&family=Nunito+Sans:wght@400;800;900&display=swap">
<style>
  :root {
    --navy: #13318f;
    --brand: #0054aa;
    --white: #ffffff;
    --wood-dark: #3a2414;
    --wood-mid: #7a4e2c;
    --wood-light: #a06a3d;
    --venue-box: #221f1f;
  }
  * { box-sizing: border-box; margin: 0; padding: 0; }
  html, body { width: 857px; height: 1200px; overflow: hidden; background: var(--white); }
  .invite {
    position: relative;
    width: 857px;
    height: 1200px;
    background: var(--white);
    font-family: "Nunito Sans", Arial, sans-serif;
    color: var(--navy);
  }
  .brand {
    position: absolute;
    top: 95px;
    left: 0;
    width: 100%;
    display: flex;
    justify-content: center;
    align-items: center;
    gap: 18px;
  }
  .brand-mark {
    width: 64px;
    height: 64px;
    background: var(--brand);
  }
  .brand-name {
    font-weight: 900;
    font-size: 68px;
    letter-spacing: 1px;
    color: var(--brand);
    line-height: 1;
  }
  .hero {
    position: absolute;
    top: 272px;
    left: 0;
    width: 857px;
    height: 418px;
  }
  .hero-photo {
    position: absolute;
    inset: 0;
    background: radial-gradient(ellipse at 50% 60%, var(--wood-light) 0%, var(--wood-mid) 45%, var(--wood-dark) 100%);
  }
  .hero-lead {
    position: absolute;
    top: 35px;
    width: 100%;
    text-align: center;
    color: var(--white);
    font-size: 31px;
    font-weight: 400;
  }
  .hero-lead strong { font-weight: 800; }
  .hero-title {
    position: absolute;
    top: 90px;
    width: 100%;
    text-align: center;
    color: var(--white);
    font-family: "Great Vibes", cursive;
    font-weight: 400;
    font-size: 128px;
    line-height: 0.98;
  }
  .intro {
    position: absolute;
    top: 735px;
    left: 40px;
    width: 777px;
    text-align: center;
    font-size: 24.5px;
    line-height: 1.5;
  }
  .intro strong { font-weight: 800; }
  .details {
    position: absolute;
    left: 69px;
    top: 893px;
    font-weight: 800;
    font-size: 25px;
    line-height: 1.45;
  }
  .details p + p { margin-top: 20px; }
  .details .address { margin-top: 30px; }
  .venue-mark {
    position: absolute;
    left: 508px;
    top: 1004px;
    width: 283px;
    height: 152px;
    background: var(--venue-box);
    display: flex;
    align-items: center;
    justify-content: center;
  }
  .venue-name {
    color: var(--white);
    font-weight: 400;
    font-size: 12px;
    letter-spacing: 7px;
    text-transform: uppercase;
  }
</style>
</head>
<body>
  <main class="invite">
    <header class="brand">
      <span class="brand-mark"></span>
      <span class="brand-name">QVR</span>
    </header>

    <section class="hero">
      <div class="hero-photo" role="img" aria-label="Overhead photo of a steakhouse table with sliced steak, sides and glasses of wine"></div>
      <p class="hero-lead"><strong>QVR</strong> invites you to join us at</p>
      <h1 class="hero-title">Chat n’ Clink<br>Evening</h1>
    </section>

    <p class="intro">Join us for excellent wine and tasty bites at our <strong>semi-annual PDA reception</strong>. Swing by whenever you can, timing is casual and we'd love to see you there!</p>

    <section class="details">
      <p>Monday, Jan 22nd<br>6:30 - 8:30 pm EST</p>
      <p>Tallow Grill<br>Lounge Room</p>
      <p class="address">48213 E Harrow Glen Rd<br>Aventura, FL 33417</p>
    </section>

    <div class="venue-mark">
      <span class="venue-name">Tallow Grill</span>
    </div>
  </main>
</body>
</html>
```